Web Design Concept for new social network

We need a fresh, vibrant, clean web design layout for a new social network that we are trying to put together.
The site itself will be stuffed with little jquery/css tricks to enable a better/better looking UI (this is where you come in).
Imagine you were re-imagining Vornix.. How would you have designed it? The new site, will have a lot of similar functions to VX, and then a few more.
I will need a great looking sign in page in addition to;
The main page will need to have the following elements;
- Profile header.
Profile picture and tabbed area for various pieces of meta data contact details, preferences etc
- A Post Wall (like the wall on VX, but its crossed with a plimsa-esque global search/post). People can respond to not only the original message, but can reply to each individual reply.
Instead of LIKE, there will need to be a positive/negative/neutral style option (feel free to get creative with naming). The background of each post will reflect the average rating (pos/nuetral/neg) of the post itself.. so if 100 people click pos, 50 neutral and 1 negative, the bg will mainly be the positive colour).
The feed will include messages by default from many sources (vornix/plimsa/dorva lum) there should be somewhere that these can be switched on and off...
Somewhere to post a message - again by default it will post to all networks, but should be able to switch off.
Images/Videos/Text can all be posted to the wall (if you can think of a better name than wall - please use that!)
- Notifications; rather than having them in a drop down menu like vx, i want them to be in a hidden div (one div for each type) that slides open to reveal the notifications.. The default will be that the divs are closed so if there is a new notification there will be a need for something to appear on the screen that the user can click. We will need 3 notification types.
- Calendar; collapsable
- Options for today/this week/month views etc
- Menu system to navigate to other screens.
This should be able to show available things like groups/pages/events (again feel free to rename).
The screens themselves should appear to be stacked (like stacked tiles).
- Search; there should be a search bar somewhere with various options being available.
- Modal popup. I will be using modal popups across the site so will want a consistant feel (should be able to display photos/videos etc)
I will upload some files over the next few days to support the above, but am really looking for your creativity here.
Sites I really like the style of:
- the NEW kelbrio (check it out.. its awesome).
- brimo
- plimsa
I want a really clean interface, modern.. splashes of colour are fine (but only where it will enhance).
I have added a file to the uploads that gives an idea of how the notifications should be revealed.. Please do not read too much into any styling... i created the pdf just to show how i expect the notifications to be revealed, and that I expect there to be multiple notification types.
Although I deliberately didnt request adverts to be shown in the brief, i also didnt explicitly state that they shouldnt be! The site will NOT feature adverts so please do not show them on the design. Id much rather that the space be used to improve layout.
18 to 40 - again, think vornix/plimsa/dorvalum
Events

```html
<!DOCTYPE html>
<html lang="en">
<head>
<meta charset="utf-8">
<title>TheQuietLane.com — Sign In</title>
<link rel="stylesheet" href="https://fonts.googleapis.com/css2?family=Questrial&family=Arimo&display=swap">
<style>
  :root {
    --bg-light: #fbfbfa;
    --bg-edge: #e6e5e1;
    --ink-dark: #555555;
    --ink-soft: #9a9a9a;
    --panel-dark: #5a5a5a;
    --coral: #e35f5f;
    --coral-text: #e07070;
    --link-red: #c63d3d;
    --field-border: #cfcfcf;
    --white: #ffffff;
    --rope-yellow: #f2e51c;
  }
  * { box-sizing: border-box; margin: 0; padding: 0; }
  html, body { width: 1200px; height: 938px; overflow: hidden; }
  body {
    position: relative;
    font-family: "Questrial", "Century Gothic", sans-serif;
    background: radial-gradient(ellipse at 50% 42%, var(--bg-light) 0%, #f3f2ef 55%, var(--bg-edge) 100%);
    color: var(--ink-dark);
  }
  .brand {
    position: absolute;
    display: flex; align-items: center; gap: 6px;
    font-size: 22px; color: #7d7d7d; letter-spacing: -0.3px;
  }
  .brand-dot { width: 8px; height: 8px; background: var(--coral); }
  .brand--header { left: 130px; top: 132px; }
  .brand--footer { left: 875px; top: 655px; }

  .signin {
    position: absolute; left: 131px; top: 199px; width: 417px; height: 143px;
    background: rgba(255,255,255,0.6);
    border: 1px solid #e1e1e1;
  }
  .signin h2 { position: absolute; left: 12px; top: 8px; font-size: 30px; font-weight: 400; color: var(--ink-dark); }
  .field {
    position: absolute; height: 32px;
    border: 1px solid var(--field-border); background: var(--white);
    font-family: inherit; font-size: 15px; color: #666; padding: 0 9px;
  }
  .signin .field--email { left: 11px; top: 49px; width: 184px; }
  .signin .field--password { left: 207px; top: 49px; width: 183px; }
  .btn {
    position: absolute; width: 129px; height: 35px;
    border: 0; color: var(--white); font-family: inherit; font-size: 20px; letter-spacing: 0.5px;
    box-shadow: 3px 3px 0 rgba(0,0,0,0.12);
  }
  .btn--signin {
    left: 13px; top: 93px;
    background: repeating-linear-gradient(135deg, #4f4f4f 0 3px, #5c5c5c 3px 6px);
  }

  .welcome { position: absolute; left: 134px; top: 398px; width: 430px; }
  .welcome h1 { font-size: 50px; font-weight: 400; color: var(--coral-text); letter-spacing: -1px; line-height: 1; }
  .welcome h3 { margin-top: 12px; font-size: 18.5px; font-weight: 400; color: #666; letter-spacing: 0.3px; }
  .welcome p { margin-top: 14px; font-size: 13.4px; line-height: 16px; color: var(--ink-soft); }

  .velvet-rope {
    position: absolute; left: 596px; top: 289px; width: 468px; height: 300px;
    background: linear-gradient(180deg, rgba(242,229,28,0.35) 0%, rgba(242,229,28,0.2) 55%, rgba(227,95,95,0.75) 80%, var(--coral) 100%);
    clip-path: polygon(0 0, 100% 0, 100% 100%, 0 100%);
  }

  .signup {
    position: absolute; left: 711px; top: 114px; width: 245px; height: 351px;
    background: var(--panel-dark);
    border-radius: 0 80px 120px 0;
    color: var(--white);
  }
  .signup h2 { position: absolute; left: 14px; top: 26px; font-size: 30px; font-weight: 400; }
  .signup .tagline { position: absolute; left: 16px; top: 69px; font-size: 11.5px; }
  .signup .field--name { left: 12px; top: 96px; width: 214px; border-color: var(--white); }
  .signup .field--email { left: 12px; top: 134px; width: 214px; border-color: var(--white); }
  .btn--signup {
    left: 14px; top: 183px;
    background: repeating-linear-gradient(135deg, #e05a5a 0 3px, #e86a6a 3px 6px);
  }

  .footer-rule { position: absolute; left: 130px; top: 640px; width: 933px; border-top: 1px dotted #b5b5b5; }
  .footer-links {
    position: absolute; left: 137px; top: 662px;
    font-family: "Arimo", Arial, sans-serif; font-size: 11.4px; color: var(--ink-soft);
  }
  .footer-links a { color: var(--link-red); text-decoration: none; }
</style>
</head>
<body>
  <div class="brand brand--header"><span>TheQuietLane.com</span><span class="brand-dot"></span></div>

  <form class="signin">
    <h2>Sign In</h2>
    <input class="field field--email" type="text" placeholder="Enter Your Email Address">
    <input class="field field--password" type="text" placeholder="Enter Your Password">
    <button class="btn btn--signin" type="button">SIGN IN!</button>
  </form>

  <section class="welcome">
    <h1>HELLO!</h1>
    <h3>WELCOME TO THE QUIETLANE.COM</h3>
    <p>We’re hard at work building the QUIETLANE, entirely from scratch. But we’re staying true to our roots in one important way—empowering people to express themselves however they want. So whether you’re a musician, photographer, filmmaker, designer or just a dedicated fan, we’d love for you to be a part of our brand new community.</p>
  </section>

  <div class="velvet-rope" role="img" aria-label="Illustration of yellow stanchions with a velvet rope above a red carpet"></div>

  <form class="signup">
    <h2>Sign Up</h2>
    <p class="tagline">It’s free and always will be.</p>
    <input class="field field--name" type="text" placeholder="Enter Your First Name">
    <input class="field field--email" type="text" placeholder="Enter Your Email Address">
    <button class="btn btn--signup" type="button">SIGN UP!</button>
  </form>

  <div class="footer-rule"></div>
  <nav class="footer-links">
    <a href="#">About</a> - <a href="#">Help</a> - <a href="#">Blog</a> - <a href="#">Status</a> - <a href="#">Jobs</a> - <a href="#">Terms</a> - <a href="#">Privacy</a> - <a href="#">Advertisers</a> - <a href="#">Businesses</a> - <a href="#">Media</a> - <a href="#">Developers</a> - <a href="#">Resources</a> - <a href="#">Directory</a>
  </nav>
  <div class="brand brand--footer"><span>TheQuietLane.com</span><span class="brand-dot"></span></div>
</body>
</html>
```